Website For Custom Home Builder

-Very elegant and simple design as I am a high end custom home builder.
-I build homes $2 million to $10 million range so the website needs to reflect the level of home that I build.
-Attached are photos of homes I have built to use as well as my logo.
-I need final design to be in layered format so my local guy can edit if he needs to.

3 Page Design
1. HomePage:
-logo, some photos,
-“Building beautiful custom homes in Indianapolis for over 20 years”
2. AboutPage:
-Wade Holloran has been building stunning custom homes in the Indianpolis area for over 20 years. As a small boutique building company we only build a handful of homes a year in order to offer our clients the personal attention that their homes deserve. It's this attention to detail that makes our client experience and final product something special and unique.
- family photo
3. ContactPage:
-office photo
-317-552-7190
-wade@whcrafted.com
-415 North Fernmill Rd, Suite 308, Carmel IN 46033

Target Market(s)

Very high end clients looking to build $2 million to $10 million homes.

Industry/Entity Type

Residential high end custom home builder/construction

Coding

Coded - Design and coding required

Number of Pages Required

3 page

Requirements
Must have
• Very simple and elegant design that represents the high end homes that I build.
Nice to have
Should not have
• Should NOT have a lot of clutter or be a very busy page from a design perspective.

```html
<!DOCTYPE html>
<html lang="en">
<head>
<meta charset="utf-8">
<title>Wade Holloran Custom Homes</title>
<link href="https://fonts.googleapis.com/css2?family=Rubik:wght@400;500;600;700&display=swap" rel="stylesheet">
<style>
:root{
  --brand:#a65b24;
  --brand-dark:#7e4217;
  --ink:#1b1b1b;
  --text:#4a4a4a;
  --paper:#ffffff;
  --cream:#f8f7f5;
  --night:#202020;
  --label:#4e4e4e;
}
*{margin:0;padding:0;box-sizing:border-box}
html,body{width:1200px;height:2438px;overflow:hidden;background:var(--paper)}
body{position:relative;font-family:"Rubik",sans-serif;color:var(--ink)}
.abs{position:absolute}
.site-header{position:absolute;left:0;width:1200px;height:82px;background:var(--paper)}
.logo{position:absolute;left:60px;top:29px;display:flex;align-items:center;gap:8px;font-size:17px;font-weight:500;color:#3b2a20;letter-spacing:.5px}
.logo-mark{width:14px;height:14px;background:#3b2a20}
.nav a{position:absolute;top:34px;font-size:12.5px;color:var(--ink);text-decoration:none;letter-spacing:.2px}
.nav a.active{color:var(--brand)}
.nav a.active::after{content:"";position:absolute;left:50%;top:20px;margin-left:-5px;border-left:5px solid transparent;border-right:5px solid transparent;border-bottom:6px solid var(--brand)}
.call{position:absolute;left:974px;top:21px;width:165px;height:41px;background:var(--brand);color:#fff;font-size:16px;display:flex;align-items:center;justify-content:center;gap:10px}
.hero{position:absolute;left:0;top:82px;width:1200px;height:585px;background:linear-gradient(180deg,#5a4a47 0%,#b4653a 18%,#d8894a 30%,#6b5448 48%,#4a3a30 62%,#6a5a3e 80%,#3f5528 90%,#2f3f22 100%)}
.hero-title{position:absolute;left:0;top:184px;width:1200px;text-align:center;color:#fff;font-size:45px;font-weight:600;line-height:58px;text-shadow:0 2px 8px rgba(0,0,0,.35)}
.hero-title span{color:#d07a34}
.bar{position:absolute;left:0;width:1200px;height:45px;background:var(--brand);color:#fff;font-size:13px;display:flex;align-items:center;justify-content:center}
.page-label{position:absolute;left:0;width:1200px;background:var(--night);color:var(--label);font-size:60px;display:flex;align-items:center;justify-content:center}
.dots{position:absolute;left:1126px;width:74px}
.dots i{display:block;width:15px;height:15px;border:1px solid var(--brand);background:transparent;margin-bottom:9px;position:relative}
.dots.light i{border-color:#fff;background:#fff}
.dots i.on{background:#fff;border-color:var(--brand)}
.dots i.on::before{content:"";position:absolute;left:3px;top:3px;width:7px;height:7px;background:var(--brand)}
.dots i.on::after{content:"";position:absolute;left:15px;top:6px;width:58px;height:1px;background:var(--brand)}
.dots.light i.on::after{background:#fff}
.section{position:absolute;left:0;width:1200px;background:var(--cream)}
.eyebrow{position:absolute;left:664px;top:1036px;font-size:21px;color:var(--brand)}
.about-title{position:absolute;left:662px;top:1074px;font-size:32px;line-height:40px;font-weight:500;color:var(--ink)}
.about-copy{position:absolute;left:667px;top:1197px;width:405px;font-size:12.5px;line-height:21px;color:var(--text)}
.about-copy p{margin-bottom:13px}
.btn{position:absolute;left:667px;top:1374px;width:139px;height:40px;background:var(--brand);color:#fff;font-size:14.5px;display:flex;align-items:center;justify-content:center}
.contact-title{position:absolute;left:0;top:1860px;width:1200px;text-align:center;font-size:34px;font-weight:500}
.contact-sub{position:absolute;left:0;top:1909px;width:1200px;text-align:center;font-size:13.5px;color:#333}
.card{position:absolute;left:113px;top:1972px;width:975px;height:337px;background:#fff;box-shadow:0 4px 18px rgba(0,0,0,.05)}
.office{position:absolute;left:0;top:0;width:487px;height:337px;background:linear-gradient(90deg,#3c3c3c 0%,#cfc9c1 30%,#b89270 55%,#ececea 56%,#f2f2f0 100%)}
.icon{position:absolute;left:556px;width:38px;height:38px;background:linear-gradient(180deg,var(--brand),var(--brand-dark));display:flex;align-items:center;justify-content:center}
.info{position:absolute;left:620px;font-size:13.5px;color:#555;line-height:24px}
.info strong{display:block;color:var(--ink);font-weight:500;font-size:15px;margin-bottom:6px}
</style>
</head>
<body>

<!-- Home page -->
<header class="site-header" style="top:0">
  <div class="logo"><span class="logo-mark"></span>WADE HOLLORAN</div>
  <nav class="nav"><a class="active" style="left:723px">HOME</a><a style="left:786px">ABOUT US</a><a style="left:871px">CONTACT US</a></nav>
  <div class="call"><svg width="18" height="18" viewBox="0 0 24 24"><path fill="#fff" d="M6.6 10.8a15.1 15.1 0 0 0 6.6 6.6l2.2-2.2c.3-.3.7-.4 1-.2 1.1.4 2.3.6 3.6.6.6 0 1 .4 1 1V20c0 .6-.4 1-1 1A17 17 0 0 1 3 4c0-.6.4-1 1-1h3.5c.6 0 1 .4 1 1 0 1.3.2 2.5.6 3.6.1.3 0 .7-.2 1z"/></svg>317-552-7190</div>
</header>
<section class="hero" role="img" aria-label="Custom stone and timber home at sunset with lit windows and a lawn">
  <h1 class="hero-title">Building beautiful custom homes<br>in Indianapolis for<br><span>over 20 years</span></h1>
</section>
<div class="dots light" style="top:319px"><i class="on"></i><i></i><i></i></div>
<div class="bar" style="top:667px">©2023 WADE HOLLORAN CUSTOM HOMES - All rights reserved.</div>
<div class="page-label" style="top:712px;height:143px">About us Page</div>

<!-- About page -->
<header class="site-header" style="top:855px">
  <div class="logo"><span class="logo-mark"></span>WADE HOLLORAN</div>
  <nav class="nav"><a style="left:723px">HOME</a><a class="active" style="left:786px">ABOUT US</a><a style="left:871px">CONTACT US</a></nav>
  <div class="call"><svg width="18" height="18" viewBox="0 0 24 24"><path fill="#fff" d="M6.6 10.8a15.1 15.1 0 0 0 6.6 6.6l2.2-2.2c.3-.3.7-.4 1-.2 1.1.4 2.3.6 3.6.6.6 0 1 .4 1 1V20c0 .6-.4 1-1 1A17 17 0 0 1 3 4c0-.6.4-1 1-1h3.5c.6 0 1 .4 1 1 0 1.3.2 2.5.6 3.6.1.3 0 .7-.2 1z"/></svg>317-552-7190</div>
</header>
<section class="section" style="top:937px;height:592px"></section>
<svg class="abs" style="left:0;top:0" width="1200" height="1529" viewBox="0 0 1200 1529">
  <defs><linearGradient id="team" x1="0" y1="0" x2="0" y2="1"><stop offset="0" stop-color="#8a9bb0"/><stop offset=".5" stop-color="#3e5570"/><stop offset="1" stop-color="#2c3a4c"/></linearGradient></defs>
  <polygon role="img" aria-label="Team of three builders in business suits" points="110,1444 110,1201 291,1076 336,1109 336,1013 547,1178 547,1444" fill="url(#team)"/>
  <line x1="547" y1="1178" x2="775" y2="1178" stroke="#7e4217" stroke-width="1.2"/>
</svg>
<div class="eyebrow">ABOUT US</div>
<h2 class="about-title">WADE HOLLORAN<br>CUSTOM HOMES</h2>
<div class="about-copy">
  <p>Wade Holloran has been building stunning custom homes in the Indianpolis area for over 20 years.</p>
  <p>As a small boutique building company we only build a handful of homes a year in order to offer our clients the personal attention that their homes deserve. It's this attention to detail that makes our client experience and final product something special and unique</p>
</div>
<div class="btn">CONTACT US</div>
<div class="dots" style="top:1189px"><i></i><i class="on"></i><i></i></div>
<div class="bar" style="top:1529px">©2023 WADE HOLLORAN CUSTOM HOMES - All rights reserved.</div>
<div class="page-label" style="top:1574px;height:142px">Contact us Page</div>

<!-- Contact page -->
<header class="site-header" style="top:1716px">
  <div class="logo"><span class="logo-mark"></span>WADE HOLLORAN</div>
  <nav class="nav"><a style="left:723px">HOME</a><a style="left:786px">ABOUT US</a><a class="active" style="left:871px">CONTACT US</a></nav>
  <div class="call"><svg width="18" height="18" viewBox="0 0 24 24"><path fill="#fff" d="M6.6 10.8a15.1 15.1 0 0 0 6.6 6.6l2.2-2.2c.3-.3.7-.4 1-.2 1.1.4 2.3.6 3.6.6.6 0 1 .4 1 1V20c0 .6-.4 1-1 1A17 17 0 0 1 3 4c0-.6.4-1 1-1h3.5c.6 0 1 .4 1 1 0 1.3.2 2.5.6 3.6.1.3 0 .7-.2 1z"/></svg>317-552-7190</div>
</header>
<section class="section" style="top:1798px;height:594px"></section>
<h2 class="contact-title">CONTACT US</h2>
<p class="contact-sub">If you have an any question please contact us today!</p>
<div class="card">
  <div class="office" role="img" aria-label="Bright open-plan office with desks, chairs and a white feature wall"></div>
  <div class="icon" style="top:50px"><svg width="20" height="20" viewBox="0 0 24 24"><path fill="none" stroke="#fff" stroke-width="1.8" d="M12 21s-6-6.2-6-11a6 6 0 0 1 12 0c0 4.8-6 11-6 11z"/><circle cx="12" cy="10" r="2.2" fill="none" stroke="#fff" stroke-width="1.8"/></svg></div>
  <div class="info" style="top:48px"><strong>WADE HOLLORAN CUSTOM HOMES</strong>415 North Fernmill Rd, Suite<br>308, Carmel IN 46033</div>
  <div class="icon" style="top:141px"><svg width="20" height="20" viewBox="0 0 24 24"><path fill="#fff" d="M6.6 10.8a15.1 15.1 0 0 0 6.6 6.6l2.2-2.2c.3-.3.7-.4 1-.2 1.1.4 2.3.6 3.6.6.6 0 1 .4 1 1V20c0 .6-.4 1-1 1A17 17 0 0 1 3 4c0-.6.4-1 1-1h3.5c.6 0 1 .4 1 1 0 1.3.2 2.5.6 3.6.1.3 0 .7-.2 1z"/></svg></div>
  <div class="info" style="top:150px">317-552-7190</div>
  <div class="icon" style="top:198px"><svg width="20" height="20" viewBox="0 0 24 24"><rect x="3" y="6" width="18" height="12" rx="1.5" fill="#fff"/><path d="M3.5 7l8.5 6 8.5-6" fill="none" stroke="#7e4217" stroke-width="1.6"/></svg></div>
  <div class="info" style="top:205px">wade@whcrafted.com</div>
</div>
<div class="dots" style="top:2097px"><i></i><i></i><i class="on"></i></div>
<div class="bar" style="top:2392px;left:5px;width:1195px;height:46px">©2023 WADE HOLLORAN CUSTOM HOMES - All rights reserved.</div>

</body>
</html>
```